Advertisement for my roofing company

Looking to get designs for:

- Secondary Logo
- Business card designs
- Small Yard Signs (like the KVL/Perch Alarm signs people put at the mail box to let bad guys know there's camera's)
- Quick Door note/flyer to leave while canvassing letting them know we are working in neighborhoods/area and want to check out their roof to see if it qualifies for roof replacement paid for by insurance.
- any other good ideas not commoningly used that is different and stands out from everyone else

We are in need of some help getting a page designed for a high school football game program packet that the school will sell to locals with all the team information in it for this years team. We are planning to do a full page for our company branding, is this something you guys can help me with? They are requesting a PDF final copy by July 1st.

Just want to advertise what we do for homeowners after a storm impacts their areas.

Basically a quick summary about our company.

We are a roofing company that specialize in storm restoration and insurance claims. Prior to the start up of vela crest me and the business partner were insurance adjuster that handle property claims after major storm event all over the country and work storm like hurricanes to snow storms that caused damage so that gives the property owner the advantage when they use us after a storm because we have over 25+ years of insurance adjusting back ground and knowledge for the major carriers people use. We also provide other services like roof repairs, gutters systems, siding, painting interior/exterior, and windows. Main focus is roofing though! We do tons of door knocking to in area that are recently impacted by storms and offer free inspections to homeowner/property owners who are concerned or curious how their roof/property held up during the storm. We also offer inspections with a Drone Inspections using SKYLOOM AI HAIL SCANNER SUITE for those people who just feel more comfortable with that. ( which is huge and helps us land lots of leads )

We proudly carry the highest residential certification with all the large roofing material manufactures. We are BRQ Sovereign Summit Select with BRQ and Ridge Keeper w/ Oakhallow which are the only two we install anymore due to the fact the rest of them are trash.

Don't use all that or anything but this just gives you a idea what we represent.

Target Market(s)

Homeowners/property owners

Industry/Entity Type

Roofing

Font styles to use
Sans Serif

Colors
EB3D1F
EC4F4E
F09395
F8D3D4
FCEDEE

Requirements
Nice to have
• Modern design look
Should not have
• Generic google/online photos.

```html
<!DOCTYPE html>
<html lang="en">
<head>
<meta charset="utf-8">
<title>Vela Crest Roofing – Door Note and Calling Cards</title>
<link rel="stylesheet" href="https://fonts.googleapis.com/css2?family=Montserrat:wght@300;400&family=Roboto:wght@400&family=Roboto+Condensed:wght@700&display=swap">
<style>
:root{
  --board:#555557;
  --red:#e41c45;
  --gold:#c9a552;
  --ink:#231f20;
  --slate:#6d6e71;
  --silver:#bcbdc0;
  --white:#ffffff;
  --display:"Montserrat",sans-serif;
  --body:"Roboto",sans-serif;
  --cond:"Roboto Condensed",sans-serif;
}
*{box-sizing:border-box;margin:0;padding:0}
html,body{width:1200px;height:849px;overflow:hidden}
body{background:var(--board);position:relative;font-family:var(--body);color:var(--white)}
.abs{position:absolute}

.board-title{font-family:var(--display);font-weight:300;font-size:39px;line-height:46px;letter-spacing:1px}
.doornote-title{left:76px;top:40px}
.card-title{left:576px;top:96px}

/* door note */
.doornote{left:216px;top:51px;width:310px;height:763px;overflow:hidden;
  background:linear-gradient(180deg,#2b2a2c 0%,#3f3f41 38%,var(--slate) 55%,var(--slate) 100%)}
.doornote .art{position:absolute;left:0;top:0}
.storm-claim{left:155px;top:100px;width:168px;text-align:center;font-family:var(--cond);font-weight:700;font-size:15.5px;line-height:16px}
.wordmark{font-family:var(--cond);font-weight:700;color:var(--white);text-transform:uppercase;line-height:1;white-space:nowrap}
.doornote .wordmark{left:26px;top:312px}
.doornote .wordmark .name{font-size:46px;display:block}
.doornote .wordmark .sub{font-size:24px;letter-spacing:3px;display:block;text-align:right;margin-top:1px}
.wordmark .dot{display:inline-block;width:.3em;height:.3em;background:var(--red);margin-right:.15em;vertical-align:middle}
.pledge{font-size:13.4px;line-height:14.8px;padding-left:9px;text-indent:-9px}
.pledge-cert{left:23px;top:404px;width:262px}
.pledge-member{left:23px;top:462px;width:190px}
.doornote .badge{left:202px;top:460px}
.services-head{left:26px;top:552px;font-family:var(--cond);font-weight:700;font-size:15px}
.services{font-size:10.4px;line-height:12px;list-style:none}
.services li::before{content:"• "}
.services-a{left:26px;top:570px}
.services-b{left:152px;top:570px}
.divider{left:32px;top:613px;width:248px;height:1px;background:#a7a8aa}
.estimate{left:26px;top:627px;font-family:var(--cond);font-weight:700;font-size:18.5px}
.estimate-phone{left:22px;top:648px;font-family:var(--cond);font-weight:700;font-size:49px;letter-spacing:-.5px}
.find-head{font-family:var(--cond);font-weight:700;font-size:11px}
.find-text{font-size:10px;line-height:13.5px}

/* cards */
.card{width:254px;height:145px;overflow:hidden}
.card svg{position:absolute;left:0;top:0}
.col-a{left:575px}.col-b{left:858px}
.row-1{top:159px}.row-2{top:350px}.row-3{top:540px}
.card .wordmark .name{font-size:18px;display:block}
.card .wordmark .sub{font-size:8px;letter-spacing:1.5px;display:block;text-align:right;margin-top:1px}
.logo-box{left:0;top:19px;width:127px;height:50px;background:var(--ink)}
.logo-box .wordmark{left:20px;top:14px}
.logo-box .wordmark .name{font-size:17px}
.person{font-size:9.5px;line-height:11px}
.person small{display:block;font-size:6.5px;line-height:9px}
.contact{font-size:5.3px;line-height:8px}
.center{text-align:center;left:0;width:254px}
.card-label{font-family:var(--display);font-weight:300;font-size:21px;white-space:nowrap}
.card-label span{font-size:14px;letter-spacing:.5px}
</style>
</head>
<body>

<div class="abs board-title doornote-title">Quick<br>Door<br>Note<br>3.5 x<br>8.5 in</div>

<section class="abs doornote">
  <svg class="art" width="310" height="763" role="img" aria-label="Photo of a home's shingled roof gable with white trim and dark siding">
    <defs>
      <linearGradient id="roofPhoto" x1="0" y1="0" x2="1" y2="1">
        <stop offset="0" stop-color="#8b7f72"/>
        <stop offset=".45" stop-color="#4d5563"/>
        <stop offset="1" stop-color="#2c3442"/>
      </linearGradient>
    </defs>
    <polygon points="0,0 310,0 0,310" fill="url(#roofPhoto)"/>
  </svg>
  <svg class="art" width="310" height="763" aria-hidden="true">
    <polygon points="310,7 160,157 310,305" fill="var(--red)"/>
    <line x1="311" y1="-1" x2="-1" y2="311" stroke="var(--gold)" stroke-width="4"/>
  </svg>

  <p class="abs storm-claim">We are a<br>roofing<br>company that<br>specialize in storm<br>restoration and<br>insurance<br>claims.</p>

  <div class="abs wordmark"><span class="name"><i class="dot"></i>Vela Crest</span><span class="sub">Roofing</span></div>

  <p class="abs pledge pledge-cert">• Proudly carry the highest residential certification with all the large roofing material manufactures.</p>
  <p class="abs pledge pledge-member">• Member of BRQ Sovereign<br>Summit Select with BRQ and<br>Ridge Keeper with<br>Oakhallow.</p>
  <svg class="abs badge" width="72" height="72" aria-hidden="true">
    <polygon points="36,3 69,36 36,69 3,36" fill="var(--ink)" stroke="var(--gold)" stroke-width="2.5"/>
  </svg>

  <h2 class="abs services-head">ROOFING SERVICES</h2>
  <ul class="abs services services-a"><li>Installation and Repair</li><li>Single Ply Systems</li><li>Built-up Roofing System</li></ul>
  <ul class="abs services services-b"><li>Waterproofing &amp; Damp-proofing</li><li>Modified Roof Systems</li><li>Siding and more...</li></ul>
  <div class="abs divider"></div>

  <p class="abs estimate">FREE ESTIMATE :</p>
  <p class="abs estimate-phone">555 014 2290</p>

  <p class="abs find-head" style="left:26px;top:711px">FIND US ON :</p>
  <p class="abs find-head" style="left:138px;top:711px">CONTACT US :</p>
  <p class="abs find-text" style="left:26px;top:726px">Porchboard<br>Snapwall</p>
  <p class="abs find-text" style="left:138px;top:726px">email ad<br>Address</p>
  <p class="abs find-text" style="left:224px;top:726px">cell number<br>land lines</p>
</section>

<h1 class="abs board-title card-title">Calling Card</h1>

<!-- option 1 -->
<div class="abs card col-a row-1" style="background:var(--silver)">
  <svg width="254" height="145" aria-hidden="true"><polygon points="160,0 254,102 254,145 26,145" fill="var(--red)"/></svg>
  <div class="abs logo-box"><div class="abs wordmark"><span class="name">Vela Crest</span><span class="sub">Roofing</span></div></div>
  <p class="abs person center" style="left:33px;top:85px">Dale Morrow<small>Manager</small></p>
  <p class="abs contact center" style="left:33px;top:112px">48 Ridge Lane, Suite 2, USA &nbsp;| &nbsp;+1 555 014 2278<br>| &nbsp;dale.morrow@velacrestroofing.com &nbsp;| &nbsp;www.velacrestroofing.com</p>
</div>
<p class="abs card-label" style="left:575px;top:305px">Option 1 <span>(Secondary Logo)</span></p>

<!-- option 2 -->
<div class="abs card col-b row-1" style="background:var(--slate)">
  <svg width="254" height="145" aria-hidden="true">
    <polygon points="226,0 254,0 254,145 82,145" fill="var(--red)"/>
    <line x1="225" y1="0" x2="79" y2="145" stroke="var(--gold)" stroke-width="2"/>
  </svg>
  <div class="abs wordmark" style="left:20px;top:24px"><span class="name" style="font-size:20px">Vela Crest</span><span class="sub">Roofing</span></div>
  <p class="abs person" style="left:21px;top:90px">Dale Morrow<small>Manager</small></p>
  <p class="abs contact" style="left:152px;top:97px">48 Ridge Lane, Suite 2, USA<br>+1 555 014 2278<br>dale.morrow@velacrestroofing.com<br>www.velacrestroofing.com</p>
</div>
<p class="abs card-label" style="left:858px;top:305px">Option 2 <span>(Primary Logo)</span></p>

<!-- option 3 -->
<div class="abs card col-a row-2" style="background:var(--ink)">
  <div class="abs wordmark" style="left:82px;top:26px"><span class="name">Vela Crest</span><span class="sub">Roofing</span></div>
  <p class="abs person center" style="top:81px">Dale Morrow<small>Manager</small></p>
  <p class="abs contact center" style="top:116px">48 Ridge Lane, Suite 2, USA &nbsp;| &nbsp;+1 555 014 2278 &nbsp;| &nbsp;dale.morrow@velacrestroofing.com<br>www.velacrestroofing.com</p>
</div>
<p class="abs card-label" style="left:575px;top:494px">Option 3 <span>(Secondary Logo)</span></p>

<!-- option 4 -->
<div class="abs card col-b row-2" style="background:var(--slate)">
  <div class="abs wordmark" style="left:79px;top:32px"><span class="name" style="font-size:20px">Vela Crest</span><span class="sub">Roofing</span></div>
  <p class="abs person" style="left:21px;top:91px">Dale Morrow<small>Manager</small></p>
  <p class="abs contact" style="left:152px;top:98px">48 Ridge Lane, Suite 2, USA<br>+1 555 014 2278<br>dale.morrow@velacrestroofing.com<br>www.velacrestroofing.com</p>
</div>
<p class="abs card-label" style="left:862px;top:494px">Option 4 <span>(Primary Logo)</span></p>

<!-- option 5 -->
<div class="abs card col-a row-3" style="background:var(--ink)">
  <svg width="254" height="145" aria-hidden="true">
    <polygon points="226,0 254,0 254,145 82,145" fill="var(--red)"/>
    <line x1="225" y1="0" x2="79" y2="145" stroke="var(--gold)" stroke-width="2"/>
  </svg>
  <div class="abs wordmark" style="left:20px;top:38px"><span class="name" style="font-size:20px">Vela Crest</span><span class="sub">Roofing</span></div>
  <p class="abs person" style="left:20px;top:90px">Dale Morrow<small>Manager</small></p>
  <p class="abs contact" style="left:148px;top:98px">48 Ridge Lane, Suite 2, USA<br>+1 555 014 2278<br>dale.morrow@velacrestroofing.com<br>www.velacrestroofing.com</p>
</div>
<p class="abs card-label" style="left:575px;top:686px">Option 5 <span>(Secondary Logo)</span></p>

<!-- option 6 -->
<div class="abs card col-b row-3" style="background:var(--red)">
  <svg width="254" height="145" aria-hidden="true"><polygon points="168,1 254,103 254,145 27,145" fill="var(--white)"/></svg>
  <div class="abs logo-box"><div class="abs wordmark"><span class="name">Vela Crest</span><span class="sub">Roofing</span></div></div>
  <p class="abs person center" style="left:33px;top:85px;color:var(--ink)">Dale Morrow<small>Manager</small></p>
  <p class="abs contact center" style="left:33px;top:112px;color:var(--ink)">48 Ridge Lane, Suite 2, USA &nbsp;| &nbsp;+1 555 014 2278<br>| &nbsp;dale.morrow@velacrestroofing.com &nbsp;| &nbsp;www.velacrestroofing.com</p>
</div>
<p class="abs card-label" style="left:862px;top:686px">Option 6 <span>(Secondary Logo)</span></p>

</body>
</html>
```